Design some Business Cards for Consultant

Most of my work is in financial & analytical consulting for microfinance and low-income housing finance, mainly in developing countries (Asia, Africa, Latin America). You can see samples of my published work here: tomasvelkind.com (main page is the blog; navigate to /papers for other published work).

Looking for a clean, no-nonsense design with limited text (name, city, website, email, skype & phone). Single-sided. Would like to print on recycled paper stock, so consider this in the design. If you can work with a (reasonably priced) online printer that ships to Belgium at reasonable cost, would pay extra for the reference and selection of appropriate paper stock, but this isn't required.

Don't hesitate if you need additional info for your design. Will provide detailed text to the contest winner.

```html
<!DOCTYPE html>
<html lang="en">
<head>
<meta charset="utf-8">
<title>Terra Ledger – Business Card</title>
<link rel="stylesheet" href="https://fonts.googleapis.com/css2?family=Open+Sans:wght@400;600;700&display=swap">
<style>
  :root {
    --backdrop: #d9d9d9;
    --card: #ffffff;
    --ink: #1f1f1f;
    --ink-soft: #3a3a3a;
    --brand-blue: #2a8fd0;
    --brand-name: #3d4a56;
  }
  * { margin: 0; padding: 0; box-sizing: border-box; }
  html, body {
    width: 1200px; height: 787px; overflow: hidden;
    background: var(--backdrop);
    font-family: "Open Sans", Arial, sans-serif;
  }
  .canvas {
    position: relative; width: 1200px; height: 787px;
    display: flex; align-items: center; justify-content: center;
  }
  .business-card {
    position: relative; width: 900px; height: 514px;
    background: var(--card);
    box-shadow: 0 4px 14px rgba(0,0,0,0.18);
  }
  .brand {
    position: absolute; top: 52px; right: 58px;
    display: flex; flex-direction: column; align-items: center; gap: 14px;
  }
  .brand-dot {
    width: 118px; height: 118px; border-radius: 50%;
    background: var(--brand-blue);
  }
  .brand-name {
    font-size: 40px; font-weight: 600; color: var(--brand-name);
    letter-spacing: 0.5px;
  }
  .identity {
    position: absolute; left: 70px; top: 170px; color: var(--ink);
  }
  .identity-name { font-size: 19px; font-weight: 700; }
  .identity-role { font-size: 17px; font-style: italic; color: var(--ink-soft); margin-bottom: 10px; }
  .identity-address { font-size: 17px; line-height: 1.25; color: var(--ink-soft); }
  .contacts {
    position: absolute; left: 58px; top: 320px;
    list-style: none; display: flex; flex-direction: column; gap: 17px;
  }
  .contact {
    display: flex; align-items: center; gap: 14px;
    font-size: 23px; color: var(--ink);
  }
  .contact-icon { width: 26px; height: 26px; flex: none; }
</style>
</head>
<body>
<main class="canvas">
  <section class="business-card">
    <div class="brand">
      <span class="brand-dot"></span>
      <span class="brand-name">TERRALEDGER</span>
    </div>

    <div class="identity">
      <p class="identity-name">Tomas Velkind, Terra Ledger</p>
      <p class="identity-role">Director</p>
      <p class="identity-address">Level 2, 118-120 Harrowgate Street<br>Fenwick VIC 3061 Australia</p>
    </div>

    <ul class="contacts">
      <li class="contact">
        <svg class="contact-icon" viewBox="0 0 26 26" aria-hidden="true">
          <circle cx="13" cy="13" r="12" fill="#1f1f1f"/>
          <path d="M9 7.5c.6-.4 1.2-.2 1.5.3l1.2 2c.3.5.1 1-.3 1.3l-.7.5c.6 1.5 1.8 2.8 3.3 3.5l.5-.7c.3-.4.9-.6 1.3-.3l2 1.2c.5.3.7.9.3 1.5-.9 1.4-2.3 1.8-3.7 1.2-2.8-1.2-4.9-3.4-6-6.2-.5-1.4 0-2.8 1.1-3.6z" fill="#fff"/>
        </svg>
        <span>1852-3961-20874</span>
      </li>
      <li class="contact">
        <svg class="contact-icon" viewBox="0 0 26 26" aria-hidden="true">
          <rect x="7" y="1.5" width="12" height="23" rx="2" fill="none" stroke="#1f1f1f" stroke-width="1.8"/>
          <line x1="11" y1="21" x2="15" y2="21" stroke="#1f1f1f" stroke-width="1.6"/>
        </svg>
        <span>438-5102-93610</span>
      </li>
      <li class="contact">
        <svg class="contact-icon" viewBox="0 0 26 26" aria-hidden="true">
          <rect x="2" y="6" width="22" height="15" fill="#1f1f1f"/>
          <path d="M2.5 6.5L13 15l10.5-8.5" fill="none" stroke="#fff" stroke-width="1.5"/>
        </svg>
        <span>info@terraledger.com</span>
      </li>
      <li class="contact">
        <svg class="contact-icon" viewBox="0 0 26 26" aria-hidden="true">
          <circle cx="13" cy="13" r="11" fill="#1f1f1f"/>
        </svg>
        <span>tomas_velkind</span>
      </li>
    </ul>
  </section>
</main>
</body>
</html>
```